Wizards Among Humbug Trades*

I am looking for a book cover which will really pop. Working title: Wizards Among Humbug Trades (or W.A.H.T. for short) The concept behind the book is: education is too expensive, screwed up, and basically failing us, and even an MBA is not worth it's name anymore! How a BS is Brilliantly Stupid, a BA is great to be a Broke Artist, an MA is Mostly Antiquated and a MS Mastered Something? ...you get the point, basically I'll be ripping into a whole bunch of degree types, then walking you through what you should actually learn from an MBA. It is going to be written with a fair bit of humor, while still being fact driven. Target audience is working professionals who are considering an MBA, or have one and want a $15 refresher of all they spent $90k+ on. No color scheme is requested, Since i do like to allow creativity to flow!

Book size 5" by 8" and ebook. Author is: L.K. Brannigan size format attached.

Went on vacation/holiday

Colors

Requirements
Must have
• W.A.H.T. (but can be an emphasises in the Wizards Among Humbug Trades title.
Nice to have
• If you look at "A quiet orchard year: notes on tending pears while raising twin goats" on quorvel, you can see a blue/silver/white color scheme I liked in the past - but dont take that as a must by any means, the second choice was a completely different (red and white) scheme

```html
<!DOCTYPE html>
<html lang="en">
<head>
<meta charset="utf-8">
<title>Wizards Among Humbug Trades — Book Cover</title>
<link rel="stylesheet" href="https://fonts.googleapis.com/css2?family=Marcellus&family=Pinyon+Script&display=swap">
<style>
  :root {
    --frame-grey: #8d8d8d;
    --frame-dark: #5f5f5f;
    --paper: #e1e1e2;
    --paper-light: #ececec;
    --ink-green: #0f3d22;
    --rosette-pale: #eef0e2;
    --rosette-mid: #c9cbb0;
    --rosette-edge: #a3a38f;
    --gold: #d6a528;
    --gold-light: #f4d25e;
    --oval-black: #1c1c1c;
  }
  html, body {
    margin: 0;
    padding: 0;
    overflow: hidden;
    background: #ffffff;
  }
  .cover {
    position: relative;
    width: 764px;
    height: 1200px;
    overflow: hidden;
    background: var(--frame-grey);
  }
  .cover-frame {
    position: absolute;
    inset: 0;
    background: linear-gradient(135deg, #a6a6a6, var(--frame-dark) 50%, #a6a6a6);
  }
  .cover-field {
    position: absolute;
    left: 52px;
    right: 52px;
    top: 40px;
    bottom: 40px;
    background: radial-gradient(ellipse at center, var(--paper-light), var(--paper) 70%);
    outline: 2px solid #cfcfcf;
  }
  .top-band {
    position: absolute;
    left: 52px;
    right: 52px;
    top: 40px;
    height: 180px;
    background: linear-gradient(180deg, #dfe3dc, #e6e7e5);
    border-bottom: 2px solid #b9c4d6;
  }
  .crest-rosette {
    position: absolute;
    left: 296px;
    top: 8px;
    width: 176px;
    height: 176px;
    border-radius: 50%;
    background: radial-gradient(circle, #f2f5ef 0%, #d8e0d4 70%, #c2cec0 100%);
  }
  .corner-rosette {
    position: absolute;
    top: 60px;
    width: 90px;
    height: 90px;
    border-radius: 50%;
    background: radial-gradient(circle, #eef2ec, #cad6c8);
  }
  .corner-rosette.left { left: 30px; }
  .corner-rosette.right { right: 30px; }
  .degree-abbr {
    position: absolute;
    left: 0;
    right: 0;
    top: 96px;
    text-align: center;
    font-family: "Marcellus", serif;
    font-size: 36px;
    letter-spacing: 1px;
    color: var(--ink-green);
  }
  .star-seal {
    position: absolute;
    left: 56px;
    top: 220px;
    width: 652px;
    height: 644px;
  }
  .rule {
    position: absolute;
    left: 276px;
    width: 212px;
    border-top: 1px solid #555;
    border-bottom: 1px solid #555;
    height: 3px;
  }
  .rule.top { top: 294px; }
  .rule.bottom { top: 754px; }
  .title {
    position: absolute;
    left: 0;
    right: 0;
    top: 300px;
    margin: 0;
    text-align: center;
    font-family: "Pinyon Script", cursive;
    font-weight: 400;
    color: var(--ink-green);
    text-shadow: 1px 1px 0 #a9b8a8;
  }
  .title-line {
    display: block;
    line-height: 1;
  }
  .title-line.big { font-size: 98px; height: 112px; }
  .title-line.small { font-size: 74px; height: 100px; }
  .awarded {
    position: absolute;
    left: 0;
    right: 0;
    top: 866px;
    text-align: center;
    font-family: "Pinyon Script", cursive;
    font-size: 27px;
    color: var(--ink-green);
  }
  .portrait-oval {
    position: absolute;
    left: 132px;
    top: 908px;
    width: 116px;
    height: 116px;
  }
  .gold-seal {
    position: absolute;
    left: 502px;
    top: 860px;
    width: 144px;
    height: 132px;
  }
  .name-plate {
    position: absolute;
    left: 300px;
    top: 980px;
    width: 170px;
    height: 110px;
    border-radius: 40%;
    background: radial-gradient(ellipse, rgba(200,200,200,0.6), rgba(225,225,226,0));
  }
  .author {
    position: absolute;
    left: 0;
    right: 0;
    top: 1018px;
    text-align: center;
    font-family: "Marcellus", serif;
    font-size: 64px;
    letter-spacing: 2px;
    color: var(--ink-green);
    text-shadow: 1px 1px 0 #a9b8a8;
    white-space: nowrap;
  }
</style>
</head>
<body>
  <main class="cover">
    <div class="cover-frame" role="img" aria-label="Grey guilloche certificate border"></div>
    <div class="cover-field" role="img" aria-label="Pale grey paper with faint white damask pattern"></div>
    <div class="top-band" role="img" aria-label="Pale green security-print band"></div>
    <div class="corner-rosette left" role="img" aria-label="Green guilloche rosette"></div>
    <div class="corner-rosette right" role="img" aria-label="Green guilloche rosette"></div>
    <div class="crest-rosette" role="img" aria-label="Green guilloche crest rosette"></div>
    <div class="degree-abbr">WAHT</div>

    <svg class="star-seal" viewBox="0 0 652 644" role="img" aria-label="Large twelve-point guilloche star rosette in cream and grey">
      <defs>
        <radialGradient id="starFill" cx="50%" cy="50%" r="50%">
          <stop offset="0%" stop-color="#b9bdb3"/>
          <stop offset="35%" stop-color="var(--rosette-pale)"/>
          <stop offset="85%" stop-color="var(--rosette-mid)"/>
          <stop offset="100%" stop-color="var(--rosette-edge)"/>
        </radialGradient>
      </defs>
      <polygon fill="url(#starFill)" stroke="#9c9c88" stroke-width="2"
        points="326,0 398,78 483,42 493,141 601,161 559,254 652,322 559,390 601,483 493,503 483,602 398,566 326,644 254,566 169,602 159,503 51,483 93,390 0,322 93,254 51,161 159,141 169,42 254,78"/>
    </svg>

    <div class="rule top"></div>
    <h1 class="title">
      <span class="title-line big">Wizards</span>
      <span class="title-line small">Among</span>
      <span class="title-line big">Humbug</span>
      <span class="title-line big">Trades</span>
    </h1>
    <div class="rule bottom"></div>

    <div class="awarded">Awarded to</div>

    <svg class="portrait-oval" viewBox="0 0 116 116" aria-hidden="true">
      <ellipse cx="58" cy="58" rx="52" ry="54" fill="#e4e4e4" stroke="var(--oval-black)" stroke-width="7" stroke-dasharray="6 3"/>
    </svg>

    <svg class="gold-seal" viewBox="0 0 144 132" aria-hidden="true">
      <defs>
        <radialGradient id="goldFill" cx="40%" cy="35%" r="70%">
          <stop offset="0%" stop-color="var(--gold-light)"/>
          <stop offset="100%" stop-color="var(--gold)"/>
        </radialGradient>
      </defs>
      <ellipse cx="72" cy="66" rx="70" ry="64" fill="url(#goldFill)"/>
    </svg>

    <div class="name-plate" role="img" aria-label="Faint grey scroll ornament"></div>
    <div class="author">L.K. BRANNIGAN</div>
  </main>
</body>
</html>
```